calloway tumbling studio

need a website for above to contain information about the academy, enrollment form etc..

Need a web design for new business Calloway Tumbling Studio offering classes in gymnastics. Info on the business is in the doc called "Web design" which details the tabs I will need on my page. Please see our Linkup page to get an idea of the style Callowaytumblingstudio.

Thank you for your help. I do not require hosting of a domain name just need it all ready to be hosted. Thanks

Budget now increased to include the coding of the website as well.

```html
<!DOCTYPE html>
<html lang="en">
<head>
<meta charset="utf-8">
<title>Calloway Tumbling Studio</title>
<link href="https://fonts.googleapis.com/css2?family=Titillium+Web:wght@400;600;700&family=Open+Sans:wght@400;600;700&family=Oswald:wght@500&display=swap" rel="stylesheet">
<style>
:root{
  --black:#000;
  --band:#121212;
  --yellow:#d4c000;
  --yellow-dark:#a89800;
  --title:#c9b800;
  --white:#fff;
  --grey:#777;
  --ink:#222;
  --blue:#5a78aa;
  --blue-dark:#3f5f98;
  --wine:#7a1a1a;
}
*{margin:0;padding:0;box-sizing:border-box}
html,body{width:684px;height:1200px;overflow:hidden;background:var(--black)}
body{position:relative;font-family:'Open Sans',sans-serif;color:var(--white)}
.abs{position:absolute}
.brand-tile{left:57px;top:21px;width:61px;height:67px;background:var(--yellow);border:2px solid var(--yellow-dark);border-radius:5px;display:flex;align-items:center;justify-content:center;text-align:center;font-family:'Titillium Web',sans-serif;font-weight:700;font-size:9px;line-height:10px;color:var(--ink)}
.nav{left:118px;top:36px;width:509px;height:38px;background:linear-gradient(#6a6a6a,#2e2e2e);display:flex;justify-content:flex-end;align-items:stretch}
.nav a{color:var(--white);text-decoration:none;font-size:7.4px;font-weight:600;display:flex;align-items:center;padding:0 10.5px}
.nav a.active{background:var(--yellow);padding:0 11px}
.slider{left:57px;top:106px;width:570px;height:307px;background:var(--white);padding:4px}
.slide-photo{width:100%;height:100%;background:radial-gradient(circle at 55% 40%,#8a8fc8,#2b3070 65%,#141a48);position:relative}
.slide-caption{left:11px;bottom:15px;font-family:'Oswald',sans-serif;font-size:16px;color:var(--white)}
.arrow{width:18px;height:18px;border-radius:50%;background:var(--white);top:149px}
.dots{left:245px;bottom:0;width:80px;height:16px;background:var(--white);border-radius:8px 8px 0 0;display:flex;justify-content:center;align-items:center;gap:4px}
.dots span{width:7px;height:7px;border-radius:50%;border:1px solid #5a6aa8}
.dots span.on{background:#111;border-color:#111}
.welcome{left:57px;top:432px;width:570px;text-align:center}
.welcome h1{font-family:'Titillium Web',sans-serif;font-weight:600;font-size:17px;color:var(--title);margin-bottom:6px}
.welcome p{font-size:6.4px;line-height:13.6px}
.section-title{font-family:'Titillium Web',sans-serif;font-weight:600;font-size:13.5px}
.yellow{color:var(--title)}
.photo{border:2px solid var(--white)}
.card h3{font-family:'Titillium Web',sans-serif;font-weight:400;font-size:9px;color:var(--title);margin:11px 0 3px}
.card p{font-size:6.6px;line-height:13.6px;width:170px}
.btn{display:inline-flex;align-items:center;justify-content:center;background:linear-gradient(#e0cc10,#b8a600);color:var(--white);font-size:6.8px;border-radius:2px}
.testimonials{left:456px;top:556px;width:170px;height:198px;background:var(--white);border-radius:5px;overflow:hidden;color:var(--ink)}
.testimonials header{height:30px;background:linear-gradient(#e2cf10,#bca900);font-family:'Titillium Web',sans-serif;font-size:9.6px;color:var(--white);padding:8px 9px}
.testimonial{padding:0 9px}
.testimonial h4{font-size:6.6px;font-weight:400;line-height:12.4px;color:var(--ink)}
.testimonial p{font-size:6.2px;line-height:12px;color:var(--grey);margin-top:3px}
.testimonial .more{text-align:right;color:var(--wine);font-size:6.2px;margin-top:1px}
.lower{left:0;top:788px;width:684px;height:256px;background:var(--band)}
.col-text{font-size:6.4px;line-height:13.6px}
.event{display:flex;gap:5px;height:48px;margin-bottom:13px}
.event .thumb{width:54px;height:48px;flex:none}
.event h5{font-size:7px;font-weight:600;color:var(--title);margin-bottom:3px}
.event p{font-size:6px;line-height:9.6px}
.side-arrow{width:13px;height:17px;background:var(--white);top:873px;display:flex;align-items:center;justify-content:center}
.promo{left:0;top:1044px;width:684px;height:81px;background:linear-gradient(var(--blue),#6080b0)}
.promo-tile{left:67px;top:17px;width:45px;height:49px;background:var(--yellow);border-radius:4px;display:flex;align-items:center;justify-content:center;text-align:center;font-family:'Titillium Web',sans-serif;font-weight:700;font-size:6.6px;line-height:7.5px;color:var(--ink)}
.promo-text{left:123px;top:9px;width:345px;font-size:9.6px;font-weight:600;line-height:18.4px}
.social-login{left:514px;top:30px;width:113px;height:23px;background:linear-gradient(var(--blue-dark),#2e4c84);border-radius:3px;display:flex;align-items:center;font-size:7.4px;font-weight:600;gap:8px;padding-left:7px}
.social-login i{width:9px;height:13px;border:1.5px solid var(--white);border-radius:2px}
.footer-links{left:56px;top:1146px;font-size:7px;line-height:15.5px}
.social{top:1149px;width:18px;height:18px;border-radius:2px}
</style>
</head>
<body>

<div class="abs brand-tile">Calloway<br>Tumbling<br>Studio</div>

<nav class="abs nav">
  <a class="active" href="#">Home</a><a href="#">About Us</a><a href="#">News &amp; Events</a><a href="#">Forms</a><a href="#">Membership</a><a href="#">Contatc Us</a>
</nav>

<section class="abs slider">
  <div class="slide-photo" role="img" aria-label="Gymnast in a red leotard performing a handstand split on the beam">
    <div class="abs slide-caption">GYMNASTICS ACADEMY</div>
  </div>
  <svg class="abs arrow" style="left:17px" viewBox="0 0 18 18"><circle cx="9" cy="9" r="9" fill="#fff"/><path d="M10.5 5.5 7 9l3.5 3.5" stroke="#333" stroke-width="1.8" fill="none"/></svg>
  <svg class="abs arrow" style="right:17px" viewBox="0 0 18 18"><circle cx="9" cy="9" r="9" fill="#fff"/><path d="M7.5 5.5 11 9l-3.5 3.5" stroke="#333" stroke-width="1.8" fill="none"/></svg>
  <div class="abs dots"><span class="on"></span><span></span><span></span></div>
</section>

<section class="abs welcome">
  <h1>Welcome To CTS</h1>
  <p>Lorem ipsum dolor sit amet, consectetuer adipiscing elit, sed diam nonummy nibh euismod tincidunt ut laoreet dolore magna aliquam erat volutpat. Ut wisi enim ad minim veniam, quis nostrud exerci tation ullamcorper suscipit lobortis nisl ut aliquip ex ea commodo consequat. Lorem ipsum dolor sit amet, consectetuer adipiscing elit, sed diam nonummy nibh euismod tincidunt ut laoreet dolore magna aliquam erat volutpat. Ut wisi enim ad minim veniam, quis nostrud exerci tation ullamcorper suscipit lobortis nisl ut aliquip ex ea commodo consequat.</p>
</section>

<h2 class="abs section-title yellow" style="left:56px;top:548px">Gymnastics</h2>

<article class="abs card" style="left:57px;top:574px">
  <div class="photo" style="width:168px;height:102px;background:linear-gradient(135deg,#2a3350,#4a5a9a 50%,#1a1a22)" role="img" aria-label="Gymnast in blue leotard on the uneven bars"></div>
  <h3>Nunc tempus felis vitae urna</h3>
  <p>Vivamus porttitor g puttrus nisi eleifend libero a tempus libero lectus feugiat felis Morbi diam</p>
  <span class="btn" style="width:71px;height:20px;margin-top:11px">READ MORE</span>
</article>

<article class="abs card" style="left:261px;top:574px">
  <div class="photo" style="width:168px;height:102px;background:linear-gradient(135deg,#6a8ab0,#c8b8b0 50%,#a03040)" role="img" aria-label="Gymnast in red white and blue leotard on the beam"></div>
  <h3>Nunc tempus felis vitae urna</h3>
  <p>Vivamus porttitor g puttrus nisi eleifend libero a tempus libero lectus feugiat felis Morbi diam</p>
  <span class="btn" style="width:71px;height:20px;margin-top:11px">READ MORE</span>
</article>

<aside class="abs testimonials">
  <header>Testimonials</header>
  <div class="testimonial" style="margin-top:10px">
    <h4>Harrowgate Mutual Partners Participating in the 2014 Wayfarers Charity Golf Classic</h4>
    <p>Harrowgate Mutual Partners is excited to participate in the 2014 Wayfarers Classic on June 23rd at Linden Hill golf course i...</p>
    <div class="more">Read more..</div>
  </div>
  <div class="testimonial" style="margin-top:6px">
    <h4>Harrowgate Mutual Partners Participating in the 2014 Wayfarers Charity Golf Classic</h4>
    <p>Harrowgate Mutual Partners is excited to participate in the 2014</p>
    <div class="more" style="margin-top:5px">Read more..</div>
  </div>
</aside>

<div class="abs lower"></div>

<h2 class="abs section-title" style="left:56px;top:803px">Acadamic</h2>
<div class="abs photo" style="left:57px;top:828px;width:181px;height:108px;background:linear-gradient(135deg,#1a2040,#5a3a7a 45%,#c850a0)" role="img" aria-label="Gymnast in pink leotard chalking her hands"></div>
<p class="abs col-text" style="left:57px;top:943px;width:183px">Lorem ipsum dolor sit amet, consectetuer adipiscing elit, sed diam nonummy nibh euismod tincidunt ut laoreet dolore magna aliquam erat volutpat. Ut wisi enim ad minim</p>
<span class="abs btn" style="left:57px;top:1005px;width:60px;height:20px">Read more...</span>

<h2 class="abs section-title" style="left:246px;top:803px">Up coming events</h2>
<div class="abs" style="left:246px;top:828px;width:186px">
  <div class="event"><div class="thumb" style="background:linear-gradient(135deg,#1a1a1a,#a82020)" role="img" aria-label="Gymnast in red leaping"></div><div><h5>Lorem ipsum dolor sit</h5><p>Lorem ipsum dolor sit amet, consectetuer adipiscing elit, sed diam nonummy nibh euismod tincidunt</p></div></div>
  <div class="event" style="margin-top:-1px"><div class="thumb" style="background:linear-gradient(135deg,#111,#4a4a5a)" role="img" aria-label="Gymnast balancing on one leg"></div><div><h5>Lorem ipsum dolor sit</h5><p>Lorem ipsum dolor sit amet, consectetuer adipiscing elit, sed diam nonummy nibh euismod tincidunt</p></div></div>
  <div class="event"><div class="thumb" style="background:linear-gradient(135deg,#111,#3a3a9a)" role="img" aria-label="Gymnast in blue leotard posing"></div><div><h5>Lorem ipsum dolor sit</h5><p>Lorem ipsum dolor sit amet, consectetuer adipiscing elit, sed diam nonummy nibh euismod tincidunt</p></div></div>
</div>
<span class="abs btn" style="left:246px;top:1005px;width:60px;height:20px">Read more...</span>

<h2 class="abs section-title" style="left:436px;top:803px">Gallery</h2>
<div class="abs photo" style="left:436px;top:828px;width:190px;height:108px;background:linear-gradient(135deg,#e8e8ee,#d060b0 55%,#f0d0e0)" role="img" aria-label="Gymnast in pink leotard in front of the rings logo"></div>
<div class="abs side-arrow" style="left:438px"><svg width="6" height="8" viewBox="0 0 6 8"><path d="M4.5 1 1.5 4l3 3" stroke="#333" stroke-width="1.4" fill="none"/></svg></div>
<div class="abs side-arrow" style="left:611px"><svg width="6" height="8" viewBox="0 0 6 8"><path d="M1.5 1l3 3-3 3" stroke="#333" stroke-width="1.4" fill="none"/></svg></div>
<p class="abs col-text" style="left:435px;top:943px;width:190px">Lorem ipsum dolor sit amet, consectetuer adipiscing elit, sed diam nonummy nibh euismod tincidunt ut laoreet dolore magna aliquam erat volutpat. Ut wisi enim ad minim</p>

<section class="abs promo">
  <div class="abs promo-tile">Calloway<br>Tumbling<br>Studio</div>
  <p class="abs promo-text">Lorem ipsum dolor sit amet, consectetuer adipiscing elit, sed diam nonummy nibh euismod tincidunt ut laoreet dolore magna aliquam erat volutpat. Ut wisi enim ad minim veniam,</p>
  <svg class="abs" style="left:469px;top:13px" width="22" height="56" viewBox="0 0 22 56"><path d="M2 2c8 0 9 4 9 12s2 13 9 14c-7 1-9 6-9 14s-1 12-9 12" stroke="#e2cf10" stroke-width="2.2" fill="none"/></svg>
  <div class="abs social-login"><i></i>Login with Linkup</div>
</section>

<footer>
  <div class="abs footer-links">Privacy &nbsp;/&nbsp; Sitemap &nbsp;/&nbsp; T&amp;C<br>Copyright © CTS. All rights reserved.</div>
  <span class="abs social" style="left:522px;background:#4a68a8"></span>
  <span class="abs social" style="left:551px;background:#5a7ca0"></span>
  <span class="abs social" style="left:581px;background:#3a9ad8"></span>
  <span class="abs social" style="left:609px;background:#d03030"></span>
</footer>

</body>
</html>
```